Brindle Loans - Morgage Broker Website

Hi. I want someone to redesign my website for Brindle Loans, We are a mortgage brokering company in Australia.

I currently have a website www.brindleloans.com.au but i do not like the design, I want clean but looking like a nice techie site but with that personal touch still.

I use wordpress and have Elementor Pro installed

Pages like on current site

Target Market(s)

Age Group 30-50, either home owners or looking to buy.

Coding

Coded - Design and coding required

Number of Pages Required

5+ page

Font styles to use
Other font styles liked:
• Ubuntu

Colors
e34298
a54499
e667a6
d3a5cc
b868aa
eea4c8

Requirements
Must have
• My Logo, and branding.. logo attached..
I want something clean and nice and vibrant!
Wordpress!
Mobile Friendly
Contact Forms
Appointment booking button
Call now button
Nice to have
• Mortgage Calculator section, and plenty of CTA's!.

Please do you research on other mortgage broker sites like quorva.com.au

```html
<!DOCTYPE html>
<html lang="en">
<head>
<meta charset="utf-8">
<title>Brindle Loans – Mortgage Broker</title>
<link rel="stylesheet" href="https://fonts.googleapis.com/css2?family=Ubuntu:wght@400;500;700&family=Poppins:wght@300;400;500;600;700;800&display=swap">
<style>
:root{
  --purple:#6a3c99;
  --purple-deep:#4f2a7c;
  --pink:#e34298;
  --pink-soft:#e667a6;
  --yellow:#f4c21b;
  --text:#555;
  --heading:#6a3c99;
  --light:#f3f1f7;
  --white:#fff;
}
*{box-sizing:border-box;margin:0;padding:0}
html,body{width:1200px;height:4121px;overflow:hidden}
body{font-family:"Poppins",sans-serif;color:var(--text);background:var(--white)}
.page{position:relative;width:1200px;height:4121px;overflow:hidden}
.abs{position:absolute}
.btn{position:absolute;display:flex;align-items:center;justify-content:center;font-family:"Poppins",sans-serif;font-weight:600;font-size:12px;text-transform:uppercase;letter-spacing:.3px;color:var(--white);text-decoration:none}
.btn--purple{background:var(--purple)}
.btn--pink{background:var(--pink)}
.btn--yellow{background:var(--yellow)}
.eyebrow{font-size:12px;text-transform:uppercase;color:var(--yellow);font-weight:500}
.section-title{font-family:"Ubuntu",sans-serif;font-weight:500;color:var(--heading)}
.photo{position:absolute}

/* header */
.site-header{position:absolute;top:0;left:0;width:1200px;height:146px;background:var(--white);border-bottom:1px solid #e5e5e5}
.brand{position:absolute;left:166px;top:58px;display:flex;align-items:center;gap:8px;font-family:"Ubuntu",sans-serif;font-weight:500;font-size:30px;color:var(--pink)}
.brand__mark{width:14px;height:14px;background:var(--yellow)}
.social{position:absolute;left:748px;top:51px;display:flex;gap:8px}
.social span{width:10px;height:10px;border-radius:50%;background:#888}
.support{position:absolute;left:860px;top:35px;display:flex;gap:14px;align-items:center}
.support__label{font-size:10px;color:#888;text-transform:uppercase}
.support__phone{font-family:"Poppins",sans-serif;font-weight:700;font-size:21px;color:#333;line-height:1.1}
.main-nav{position:absolute;top:114px;left:172px;width:860px;display:flex;justify-content:space-between;font-size:11px;font-weight:600;text-transform:uppercase;color:#333}
.main-nav .is-active{color:var(--pink)}

/* hero */
.hero{position:absolute;top:147px;left:0;width:1200px;height:680px}
.hero__photo{position:absolute;inset:0;background:linear-gradient(90deg,#8a6a56 0%,#5d4a42 35%,#6f6660 60%,#a59a92 100%)}
.hero__shade{position:absolute;inset:0;background:rgba(20,14,30,.45)}
.hero__welcome{position:absolute;top:176px;width:100%;text-align:center;color:var(--yellow);font-size:17px;text-transform:uppercase}
.hero__title{position:absolute;top:218px;width:100%;text-align:center;font-family:"Ubuntu",sans-serif;font-weight:700;font-size:36px;line-height:45px;color:var(--white)}
.hero__rate{position:absolute;top:324px;width:100%;text-align:center;font-size:22px;color:var(--yellow)}
.loan-types{position:absolute;top:608px;left:172px;width:870px;display:flex;justify-content:space-between;color:var(--white);font-size:14px;font-weight:500;text-transform:uppercase}
.loan-types li{list-style:none;display:flex;align-items:center;gap:8px}

/* about */
.about__text{position:absolute;left:610px;top:950px;width:410px}
.about__text h2{font-size:31px;line-height:36px;margin:14px 0 28px}
.about__text p{font-size:10.5px;line-height:20px;margin-bottom:20px}

/* services */
.services-bg{position:absolute;top:1400px;left:0;width:1200px;height:637px;background:linear-gradient(#fff,#eeebf4 40%,#eeebf4)}
.service-card{position:absolute;top:1622px;width:207px;height:300px;background:#f5f5f7;box-shadow:0 2px 8px rgba(0,0,0,.08);text-align:center}
.service-card__img{height:148px}
.service-card h3{font-size:12px;font-weight:600;color:var(--purple);text-transform:uppercase;margin:0 0 6px}
.service-card p{font-size:10px;line-height:13px;color:#777;padding:0 18px}
.service-card a{display:inline-block;margin-top:6px;font-size:11px;color:var(--pink)}
.service-card svg{margin:20px auto 6px;display:block}

/* cta band */
.cta-band{position:absolute;top:2037px;left:0;width:1200px;height:360px;background:linear-gradient(90deg,#4a2c6e,#5a3089 50%,#4b2b72)}
.cta-band h2{position:absolute;top:84px;width:100%;text-align:center;font-family:"Poppins",sans-serif;font-weight:700;font-size:44px;line-height:44px;color:var(--white);letter-spacing:1px}
.cta-band p{position:absolute;top:192px;width:100%;text-align:center;color:var(--white);font-size:17px;line-height:19px}

/* features */
.features__title{position:absolute;left:160px;top:2545px;font-family:"Ubuntu",sans-serif;font-weight:700;font-size:31px;line-height:36px;color:var(--purple)}
.checklist{position:absolute;left:185px;top:2685px;list-style:none;font-size:13px;color:#444}
.checklist li{display:flex;align-items:center;gap:12px;height:30px}
.work{position:absolute;left:637px;top:2995px;width:375px;color:var(--white)}
.work h2{font-family:"Ubuntu",sans-serif;font-weight:500;font-size:30px;color:var(--white);margin:8px 0 20px}
.work p{font-size:11px;line-height:20px;margin-bottom:20px}

/* calculator */
.calc-bg{position:absolute;top:3500px;left:0;width:1200px;height:490px;background:linear-gradient(90deg,#dcdde6,#f6f6f9 40%,#f6f6f9 60%,#e2dfe8)}
.calc h2{position:absolute;top:3620px;width:100%;text-align:center;font-size:35px}
.calc__lead{position:absolute;top:3692px;left:250px;width:700px;text-align:center;font-size:12.5px;line-height:19px;color:#333}
.calc__note{position:absolute;top:3870px;left:235px;width:730px;text-align:center;font-size:10.5px;line-height:19px;font-style:italic;color:#444}

.site-footer{position:absolute;top:3990px;left:0;width:1200px;height:131px;background:var(--purple);color:var(--white);text-align:center;font-size:13px;line-height:19px;padding-top:34px}
</style>
</head>
<body>
<div class="page">

<header class="site-header">
  <div class="brand"><span>Brindle Loans</span><span class="brand__mark"></span></div>
  <div class="social" aria-label="Social links"><span></span><span></span><span></span><span></span></div>
  <div class="support">
    <svg width="32" height="30" viewBox="0 0 32 30"><path d="M2 2h22v16H10l-6 5v-5H2z" fill="var(--purple)"/><path d="M26 8h4v14h-2v4l-5-4H12v-2h14z" fill="var(--purple)"/></svg>
    <div><div class="support__label">Contact for support</div><div class="support__phone">+123 555 019</div></div>
  </div>
  <nav class="main-nav">
    <span class="is-active">Home</span><span>Understanding loan types</span><span>Our services</span><span>Mortgage calculator</span><span>About us</span><span>Why use broker</span><span>Blog</span>
  </nav>
</header>

<section class="hero">
  <div class="hero__photo" role="img" aria-label="A couple meeting a mortgage broker at a desk with coins and a small model house"></div>
  <div class="hero__shade"></div>
  <div class="hero__welcome">Welcome to Brindle Loans</div>
  <h1 class="hero__title">We are PASSASIONATE about helping<br>YOU achieve your financial goals!</h1>
  <div class="hero__rate">We have fixed rates starting at 2.29%* p.a.</div>
  <a class="btn btn--pink" style="left:384px;top:418px;width:202px;height:57px">I want to buy a home</a>
  <a class="btn btn--yellow" style="left:611px;top:418px;width:204px;height:57px;color:#6a3c99">I want to refinance</a>
  <ul class="loan-types">
    <li><svg width="34" height="32" viewBox="0 0 34 32" fill="none" stroke="#fff" stroke-width="1.6"><path d="M4 15L17 4l13 11M8 12v16h18V12"/><rect x="14" y="18" width="6" height="10"/></svg>Home loans</li>
    <li><svg width="34" height="32" viewBox="0 0 34 32" fill="none" stroke="#fff" stroke-width="1.6"><circle cx="11" cy="9" r="5"/><path d="M2 28c0-7 4-11 9-11s9 4 9 11"/><circle cx="25" cy="12" r="4"/><path d="M22 28h10c0-5-3-8-7-8"/></svg>Personal loans</li>
    <li><svg width="34" height="32" viewBox="0 0 34 32" fill="none" stroke="#fff" stroke-width="1.6"><path d="M5 20l3-9h18l3 9v7H5z"/><circle cx="10" cy="23" r="2"/><circle cx="24" cy="23" r="2"/><path d="M5 20h24"/></svg>Car loans</li>
    <li><svg width="34" height="32" viewBox="0 0 34 32" fill="none" stroke="#fff" stroke-width="1.6"><path d="M3 28l10-10 6 5 12-14"/><path d="M24 8h8v8"/><path d="M4 18l6-5 4 3"/></svg>Investment loans</li>
  </ul>
</section>

<section class="about">
  <svg class="abs" style="left:160px;top:925px" width="420" height="490" viewBox="0 0 420 490">
    <path d="M42 3l-40 40M50 3L8 45M58 3L16 47M66 5L24 49M72 9L32 51" stroke="var(--pink)" stroke-width="2"/>
    <circle cx="217" cy="190" r="197" fill="none" stroke="var(--pink)" stroke-width="6" stroke-dasharray="560 90 400 190"/>
    <circle cx="217" cy="190" r="190" fill="#d8b46a"/>
    <circle cx="296" cy="365" r="116" fill="none" stroke="var(--pink)" stroke-width="7"/>
    <circle cx="296" cy="365" r="108" fill="#3f5c9a"/>
  </svg>
  <div class="photo" role="img" aria-label="Young couple smiling while reviewing loan papers and a phone" style="left:187px;top:925px;width:380px;height:380px;border-radius:50%;background:linear-gradient(135deg,#b59a7a,#d7bb6e 60%,#c79a3c)"></div>
  <div class="photo" role="img" aria-label="Portrait of the company founder in a blue suit" style="left:348px;top:1182px;width:216px;height:216px;border-radius:50%;background:linear-gradient(#d9dbe0,#4d6aa6 70%)"></div>
  <div class="about__text">
    <div class="eyebrow">About company</div>
    <h2 class="section-title">We Focus on your needs,<br>not the banks</h2>
    <p>It is far too often that you hear of people ending up with the wrong type of loan, a bad deal, or sign up with promises that are never kept. Well, I am in the business of making sure that never happens to you.</p>
    <p>Hello! My name is Daniel Moravec, and I am the founder and owner of Brindle Loans, a finance and brokerage company based on transparency, trust, and complete 360 support. After a decade of experience within banking and loan operations and seeing firsthand how the customers get pushed aside, I decided to leverage my passion for customer advocacy to provide an all-around positive experience every time.</p>
  </div>
  <a class="btn btn--purple" style="left:610px;top:1330px;width:163px;height:50px">Learn more</a>
</section>

<section class="services">
  <div class="services-bg"></div>
  <h2 class="section-title abs" style="left:160px;top:1538px;font-size:30px">What Can Brindle Loans Do for You?</h2>
  <div class="photo" role="img" aria-label="Woman reading documents at a desk with a calculator" style="left:0;top:1590px;width:380px;height:447px;background:linear-gradient(120deg,#e9e5e2,#d9c8b2 45%,#c9c7ce)"></div>
  <article class="service-card" style="left:390px">
    <div class="service-card__img" role="img" aria-label="Hands passing a small model house" style="background:linear-gradient(#dfe8ee,#c8b8a8)"></div>
    <svg width="28" height="28" viewBox="0 0 28 28" fill="none" stroke="var(--pink)" stroke-width="1.5"><path d="M4 13L14 4l10 9M7 11v13h14V11"/><rect x="11" y="16" width="6" height="8"/></svg>
    <h3>Home loans</h3><p>Your home loan is likely to be one of your life's biggest…</p><a>Learn More</a>
  </article>
  <article class="service-card" style="left:612px">
    <div class="service-card__img" role="img" aria-label="Person with calculator beside a small model house" style="background:linear-gradient(#ece7e0,#cbb9a6)"></div>
    <svg width="28" height="28" viewBox="0 0 28 28" fill="none" stroke="var(--pink)" stroke-width="1.5"><rect x="5" y="4" width="18" height="20" rx="2"/><path d="M9 9h10M9 14h4M15 14h4M9 19h4M15 19h4"/></svg>
    <h3>Refinance</h3><p>Refinancing refers to the process of paying out your current…</p><a>Learn More</a>
  </article>
  <article class="service-card" style="left:833px">
    <div class="service-card__img" role="img" aria-label="Hands reviewing financial charts on a laptop" style="background:linear-gradient(#dfe4ea,#9aa6b6)"></div>
    <svg width="28" height="28" viewBox="0 0 28 28" fill="none" stroke="var(--pink)" stroke-width="1.5"><path d="M3 24l8-8 5 4 9-11"/><path d="M19 8h6v6"/></svg>
    <h3>Investment loans</h3><p>Would you like to make your money work for you? Use…</p><a>Learn More</a>
  </article>
</section>

<section class="cta-band" role="img" aria-label="Purple-tinted background of a calculator and magnifier over financial papers">
  <h2>GIVE US A CHANCE TO MAKE<br>A DIFFERENCE!</h2>
  <p>We're all about helping you reach your next financial goal—great rates,<br>less fees, unprecedented service, and awesome loan help.</p>
  <a class="btn btn--yellow" style="left:524px;top:253px;width:152px;height:57px;color:#333">Book in now</a>
</section>

<section class="features">
  <div class="eyebrow abs" style="left:160px;top:2510px">Features</div>
  <h2 class="features__title">We assess &amp; tailor your<br>mortgage to suit your<br>financial situation</h2>
  <ul class="checklist">
    <li><svg width="18" height="14" viewBox="0 0 18 14"><path d="M1 7l5 5L17 1" fill="none" stroke="#555" stroke-width="2"/></svg>We listen to you and learn</li>
    <li><svg width="18" height="14" viewBox="0 0 18 14"><path d="M1 7l5 5L17 1" fill="none" stroke="#555" stroke-width="2"/></svg>We create breathing space for you</li>
    <li><svg width="18" height="14" viewBox="0 0 18 14"><path d="M1 7l5 5L17 1" fill="none" stroke="#555" stroke-width="2"/></svg>We develop your Mortgage plan</li>
    <li><svg width="18" height="14" viewBox="0 0 18 14"><path d="M1 7l5 5L17 1" fill="none" stroke="#555" stroke-width="2"/></svg>We select the right financial institution</li>
    <li><svg width="18" height="14" viewBox="0 0 18 14"><path d="M1 7l5 5L17 1" fill="none" stroke="#555" stroke-width="2"/></svg>We help build your secure future</li>
  </ul>
  <a class="btn btn--purple" style="left:160px;top:2890px;width:163px;height:49px">Book in now</a>

  <div class="abs" style="left:603px;top:2858px;width:435px;height:612px;background:var(--purple)"></div>
  <div class="abs" style="left:160px;top:3003px;width:450px;height:467px;background:var(--purple)"></div>
  <div class="photo" role="img" aria-label="Smiling couple holding house keys and a small model house" style="left:625px;top:2528px;width:385px;height:392px;background:linear-gradient(#f0f0f2,#d8d4d8);box-shadow:0 3px 10px rgba(0,0,0,.15)"></div>
  <div class="photo" role="img" aria-label="Friendly broker in a suit reaching out for a handshake" style="left:193px;top:3112px;width:384px;height:388px;background:linear-gradient(#f3f3f5,#cfcdd3);box-shadow:0 3px 10px rgba(0,0,0,.2)"></div>
  <div class="work">
    <div class="eyebrow">Our work</div>
    <h2>How We Work With You</h2>
    <p>Brindle Loans manage the entire process for you from start to finish and as every one of our clients is different, we fully assess your individual situation and provide a solution to meet your particular needs. Quite simply, we do everything necessary to get you the best possible rate and importantly get your loan over the line. You don't do anything except allow us to act on your behalf.</p>
    <p>Regardless of whether you require $100,000, $1,000,000 or $5 million, we consider it a privilege to be entrusted with finding you the most appropriate loan, as well as navigating the different challenges of organising your mortgage.</p>
    <p>When you partner with us, you don't need to repeat yourself to a different bank employee every time you call. Our kind of personal service has resulted in a loyal clientele of repeat business and word-of-mouth referrals, which is the primary means by which we've built our business.</p>
  </div>
</section>

<section class="calc">
  <div class="calc-bg" role="img" aria-label="Faded background of hands using a calculator over paperwork"></div>
  <h2 class="section-title">Mortgage Calculator</h2>
  <p class="calc__lead">Our Mortgage Repayment financial calculator can help you estimate how much you can borrow and what your repayments will be.</p>
  <a class="btn btn--purple" style="left:472px;top:3816px;width:256px;height:48px">Repayment calculator</a>
  <p class="calc__note">NOTE: The results from this calculator should be used as an indication only. Results do not represent quotes or Pre-qualifications for loans. Please also note that individual lenders apply different formulas and information such as default figures are again subject to individual lenders terms and conditions.</p>
</section>

<footer class="site-footer">
  Brindle Loans (Moravec Group Pty Ltd) ACN: 612 400 908. Credit Representative 508271 is authorised under<br>
  Australian Credit Licence Number 391706.<br>
  © Copyright 2020 | All Rights Reserved Brindle Loans . Privacy Policy
</footer>

</div>
</body>
</html>
```